Bold Website Redesign for a Disruptive Training Brand

Brightmoor Labs is a bold, no-fluff sales & leadership training company powered by AI-driven practice and behavioral science. We’ve already built our website structure and copy in Craftly.io — now we need a designer to fully transform the visual design across all pages (Home, Approach, Programs, About, Contact).
We’re looking for a modern, memorable, high-performance aesthetic that blends human energy, science, and tech without feeling corporate or safe. Clean, bold typography, fluid layout, strong emotional hero moments, subtle motion, and imagery that mixes real people with abstract scientific/tech visuals.Because our clients are primarily North American, please ensure any human photography or AI-generated imagery reflects a North American business context and demographics (modern, diverse, and realistic).

Your job is visual redesign only — no coding required.
The final design must be practical to rebuild inside Craftly.io.

A full, detailed creative brief (plus logo files) is included in the uploaded files.
If you can bring a mix of edge, intelligence, and strong visual storytelling, we’d love to see your work.

Website is already built in Craftly.io at - https://brightmoor-website-tempdesign.craftly.app — structure is set, visuals need redesign.

```html
<!DOCTYPE html>
<html lang="en">
<head>
<meta charset="utf-8">
<title>Brightmoor Labs — Training That Practices Back</title>
<link href="https://fonts.googleapis.com/css2?family=IBM+Plex+Sans:wght@300;400;700&family=Roboto:wght@300;400;500;700&display=swap" rel="stylesheet">
<style>
:root{
  --navy:#0a1730;
  --navy-deep:#081327;
  --blue:#3f5bf0;
  --cyan:#22e6f2;
  --teal:#26d7c9;
  --white:#ffffff;
  --muted:#c9d3e6;
  --grad:linear-gradient(90deg,var(--blue),var(--cyan));
  --grad-band:linear-gradient(100deg,#3c57e9 0%,#2a8ee0 45%,#26cfd3 100%);
}
*{box-sizing:border-box;margin:0;padding:0}
html,body{width:1200px;height:3066px;overflow:hidden;background:var(--navy);color:var(--white);font-family:"Roboto",sans-serif}
.page{position:relative;width:1200px;height:3066px}
.wrap{position:absolute;left:144px;width:912px}
.heading{font-family:"IBM Plex Sans",sans-serif;font-weight:300;text-transform:uppercase;line-height:1.2}
.heading b{font-weight:700}
.rule{display:block;width:72px;height:2px;background:var(--cyan);margin:6px auto 0}
.btn{display:inline-flex;align-items:center;justify-content:center;gap:8px;height:44px;padding:0 24px;border-radius:3px;font-size:14px;font-weight:500;text-transform:uppercase;text-decoration:none}
.btn-grad{background:var(--grad);color:var(--white)}
.btn-white{background:var(--white);color:var(--blue)}

/* top bar */
.topbar{position:absolute;top:0;left:0;width:1200px;height:48px;background:#0d1a33;display:flex;justify-content:flex-end;align-items:center;padding-right:144px;gap:26px;font-size:15px}
.topbar .item{display:flex;align-items:center;gap:8px;color:var(--white)}
.topbar .btn{height:40px;padding:0 18px;font-size:13px;border-radius:3px;background:linear-gradient(90deg,#3a63f2,#27d2ec)}
/* nav */
.nav{position:absolute;top:48px;left:0;width:1200px;height:110px;background:var(--navy)}
.brand{position:absolute;left:144px;top:36px;font-family:"Roboto",sans-serif;font-weight:700;font-size:19px;letter-spacing:3px;text-transform:uppercase;display:flex;align-items:center;gap:10px}
.brand .dot{width:22px;height:22px;border-radius:50%;background:var(--cyan)}
.menu{position:absolute;left:396px;top:0;height:110px;display:flex;font-size:15px;font-weight:700}
.menu a{display:flex;align-items:center;padding:0 18px;color:var(--white);text-decoration:none;height:110px}
.menu a.active{background:linear-gradient(180deg,#2fc3ef,#3d5af1)}
.nav .divider{position:absolute;left:939px;top:30px;width:1px;height:52px;background:#3a4866}
.social{position:absolute;display:flex;gap:28px}
.social span{width:22px;height:22px;border-radius:50%;border:2px solid #8b94a6;display:block}

/* hero */
.hero{position:absolute;top:158px;left:0;width:1200px;height:598px;background:radial-gradient(ellipse at 65% 45%,#6c86a8 0%,#3b5578 35%,#1d3150 70%,#142441 100%)}
.hero-copy{position:absolute;left:144px;top:124px;width:520px}
.hero-copy h1{font-size:43px;letter-spacing:.5px}
.hero-copy p{margin-top:12px;font-size:21px;line-height:32px;font-weight:500}
.hero-copy .actions{margin-top:24px;display:flex;gap:8px}
.hero-copy .btn{width:174px}
.hero-shape{position:absolute;left:0;top:574px;width:1200px;height:182px}

/* problem */
.problem{top:860px;text-align:center}
.problem h2{font-size:39px}
.problem p{margin-top:28px;font-size:19.5px;line-height:29px;padding:0 0}
.problem .link{display:inline-block;margin-top:22px;color:#4563f5;font-size:20px;font-weight:500;text-decoration:none}

/* team band */
.team{position:absolute;top:1220px;left:0;width:1200px;height:504px;background:var(--grad-band)}
.team-photo{position:absolute;left:144px;top:30px;width:446px;height:462px;border-radius:4px;background:linear-gradient(160deg,rgba(255,255,255,.35),rgba(30,60,140,.35))}
.team-copy{position:absolute;left:631px;top:92px;width:430px}
.team-copy h2{font-size:33px;line-height:40px}
.team-copy .rule{margin:8px 0 0;width:72px;background:var(--white)}
.team-copy p{margin-top:24px;font-size:15.5px;line-height:24px}
.team-copy .btn{margin-top:28px;width:157px}

/* practice */
.practice{top:1818px;text-align:center}
.practice h2{font-size:39px}
.practice .lead{margin-top:16px;font-size:20px}
.cards{margin-top:34px;display:flex;gap:25px}
.card{width:287px;height:280px;border-radius:28px;border:1.5px solid #1fb6c9;padding:36px 20px 0;text-align:center}
.card .icon{width:86px;height:86px;border-radius:50%;background:var(--white);margin:0 auto;display:flex;align-items:center;justify-content:center}
.card h3{margin-top:24px;font-size:20px;font-weight:500}
.card p{margin-top:10px;font-size:15.5px;line-height:24px}

/* cta */
.cta{position:absolute;top:2321px;left:0;width:1200px;height:417px;background:var(--grad-band);text-align:center}
.cta h2{margin-top:88px;font-size:39px}
.cta p{margin:24px auto 0;width:780px;font-size:20px;line-height:29px}
.cta .btn{margin-top:20px;width:213px;height:45px}

/* footer */
.footer{position:absolute;top:2738px;left:0;width:1200px;height:328px;background:var(--navy)}
.footer .brand{top:118px;font-size:20px}
.col{position:absolute;top:70px}
.col h4{font-size:16px;font-weight:500;text-transform:uppercase;padding-bottom:6px;position:relative}
.col h4::after{content:"";position:absolute;left:0;bottom:0;width:38px;height:1.5px;background:var(--cyan)}
.col ul{list-style:none;margin-top:18px;font-size:13px;line-height:29px}
.contact li{display:flex;gap:14px;margin-bottom:18px;font-size:13px;line-height:22px}
.contact .ic{width:26px;height:26px;border-radius:50%;background:#142a4a;display:flex;align-items:center;justify-content:center;flex:none}
.subscribe .field{margin-top:22px;width:219px;height:34px;border-radius:17px;background:var(--white);display:flex;overflow:hidden}
.subscribe .field span{flex:1;color:#333;font-size:10px;display:flex;align-items:center;gap:5px;padding-left:14px}
.subscribe .field b{width:45px;background:var(--grad);display:flex;align-items:center;justify-content:center}
.footer .line{position:absolute;left:144px;top:270px;width:912px;height:1px;background:#1f2d48}
.footer .copy{position:absolute;top:288px;left:0;width:1200px;text-align:center;font-size:12px}
</style>
</head>
<body>
<div class="page">

  <header>
    <div class="topbar">
      <span class="item">
        <svg width="14" height="14" viewBox="0 0 24 24"><path fill="#22e6f2" d="M6.6 10.8a15 15 0 0 0 6.6 6.6l2.2-2.2a1 1 0 0 1 1-.25 11 11 0 0 0 3.6.6 1 1 0 0 1 1 1V20a1 1 0 0 1-1 1A17 17 0 0 1 3 4a1 1 0 0 1 1-1h3.5a1 1 0 0 1 1 1 11 11 0 0 0 .6 3.6 1 1 0 0 1-.25 1z"/></svg>
        +1 (555) 014-2290
      </span>
      <span class="item">
        <svg width="15" height="12" viewBox="0 0 24 18"><rect x="1" y="1" width="22" height="16" rx="2" fill="none" stroke="#22e6f2" stroke-width="2"/><path d="M1 2l11 8 11-8" fill="none" stroke="#22e6f2" stroke-width="2"/></svg>
        hello@brightmoorlabs.com
      </span>
      <a class="btn" href="#">
        <svg width="14" height="12" viewBox="0 0 24 20"><path fill="#fff" d="M9 1C4 1 0 4 0 7.5c0 2 1.2 3.7 3 4.8L2 16l4-2.3c1 .3 2 .4 3 .4 5 0 9-3 9-6.6S14 1 9 1z"/></svg>
        Let’s Talk
      </a>
    </div>
    <nav class="nav">
      <div class="brand"><span class="dot"></span>Brightmoor Labs</div>
      <div class="menu">
        <a class="active" href="#">HOME</a>
        <a href="#">APPROACH</a>
        <a href="#">PROGRAMS</a>
        <a href="#">ABOUT</a>
        <a href="#">CONTACT</a>
      </div>
      <span class="divider"></span>
      <div class="social" style="left:979px;top:44px"><span aria-label="Professional network"></span><span aria-label="Social feed"></span></div>
    </nav>
  </header>

  <section class="hero" role="img" aria-label="Blurred close-up of a glassy molecular structure in blue tones">
    <div class="hero-copy">
      <h1 class="heading">Training that<br><b>practices back</b></h1>
      <p>You'll see measurable growth as your people turn insight into habit — automatically, sustainably, and without extra work for their leaders.</p>
      <div class="actions">
        <a class="btn btn-grad" href="#">See how we do it</a>
        <a class="btn btn-white" href="#">
          <svg width="14" height="12" viewBox="0 0 24 20"><path fill="#3f5bf0" d="M9 1C4 1 0 4 0 7.5c0 2 1.2 3.7 3 4.8L2 16l4-2.3c1 .3 2 .4 3 .4 5 0 9-3 9-6.6S14 1 9 1z"/></svg>
          Let’s Talk
        </a>
      </div>
    </div>
  </section>
  <svg class="hero-shape" viewBox="0 0 1200 182" preserveAspectRatio="none" aria-hidden="true">
    <defs>
      <linearGradient id="bandLeft" x1="0" x2="1"><stop offset="0" stop-color="#3f7ff0"/><stop offset="1" stop-color="#4a63f4"/></linearGradient>
      <linearGradient id="bandRight" x1="0" x2="1"><stop offset="0" stop-color="#22c9ee"/><stop offset="1" stop-color="#22f2f7"/></linearGradient>
    </defs>
    <polygon points="0,64 600,182 1200,64 1200,182 0,182" fill="#0a1730"/>
    <polygon points="0,8 600,182 0,64" fill="url(#bandLeft)"/>
    <polygon points="1200,8 1200,64 600,182" fill="url(#bandRight)"/>
  </svg>

  <section class="wrap problem">
    <h2 class="heading">The real problem isn't your people —<br>it's the <b>forgetting curve</b></h2>
    <span class="rule"></span>
    <p>Within a week, most training disappears. Leaders are left guessing who's using what they learned — and no one has time to fix it. We built Brightmoor Labs to make progress automatic, measurable, and real.</p>
    <a class="link" href="#">Watch how sustained practice changes the curve ⟶</a>
  </section>

  <section class="team">
    <div class="team-photo" role="img" aria-label="Smiling woman sitting cross-legged with a laptop, giving a thumbs up"></div>
    <div class="team-copy">
      <h2 class="heading">Built by people<br>who've led the <b>change<br>themselves</b></h2>
      <span class="rule"></span>
      <p>Behind Brightmoor Labs are leaders who've lived the challenge of making learning last. They've scaled companies, built cultures, and led transformation — and now they've designed the system they always wished existed.</p>
      <a class="btn btn-white" href="#">Meet the team</a>
    </div>
  </section>

  <section class="wrap practice">
    <h2 class="heading">Practice made <b>permanent</b></h2>
    <span class="rule"></span>
    <p class="lead">You'll replace "hope they remember" with a system that makes sure they do.</p>
    <div class="cards">
      <article class="card">
        <div class="icon"><svg width="48" height="48" viewBox="0 0 48 48" fill="none" stroke="#3f5bf0" stroke-width="2"><path d="M16 40v-7c-5-3-7-8-6-13 2-8 10-12 18-10 7 2 10 8 9 14l3 5-3 1v5h-6v5"/><circle cx="24" cy="21" r="5" stroke="#22c9ee"/><path d="M24 12v4M24 26v4M15 21h4M29 21h4" stroke="#22c9ee"/></svg></div>
        <h3>LEARN</h3>
        <p>Fast, focused workshops, built on science, that install the mindset and skills that matter most.</p>
      </article>
      <article class="card">
        <div class="icon"><svg width="48" height="48" viewBox="0 0 48 48" fill="none" stroke="#3f5bf0" stroke-width="2"><rect x="12" y="6" width="22" height="32" rx="2"/><path d="M17 13h12M17 18h12M17 23h8" stroke="#22c9ee"/><circle cx="32" cy="34" r="5" stroke="#22c9ee"/><path d="M30 38l-1 6 3-2 3 2-1-6"/></svg></div>
        <h3>CERTIFY</h3>
        <p>Programmatic AI-driven practice and feedback - mastery without management overhead.</p>
      </article>
      <article class="card">
        <div class="icon"><svg width="48" height="48" viewBox="0 0 48 48" fill="none" stroke="#3f5bf0" stroke-width="2"><circle cx="24" cy="24" r="18"/><circle cx="24" cy="20" r="4" stroke="#22c9ee"/><path d="M16 32c1-5 4-7 8-7s7 2 8 7" stroke="#22c9ee"/><circle cx="14" cy="22" r="3"/><circle cx="34" cy="22" r="3"/></svg></div>
        <h3>SUSTAIN</h3>
        <p>Light-touch challenges and dashboards that keep skills sharp long after training ends.</p>
      </article>
    </div>
  </section>

  <section class="cta">
    <h2 class="heading">Ready to see what<br><b>lasting capability</b> looks like?</h2>
    <p>Lasting growth starts with one — a real conversation about what's working, what's not, and what's possible.</p>
    <a class="btn btn-white" href="#">Start a conversation</a>
  </section>

  <footer class="footer">
    <div class="brand"><span class="dot"></span>Brightmoor Labs</div>
    <div class="col" style="left:423px">
      <h4>Site Map</h4>
      <ul><li>Home</li><li>Approach</li><li>Programs</li><li>About</li><li>Contact</li></ul>
    </div>
    <div class="col contact" style="left:582px">
      <h4>Contact Info</h4>
      <ul style="margin-top:20px">
        <li><span class="ic"><svg width="11" height="11" viewBox="0 0 24 24"><path fill="#22e6f2" d="M6.6 10.8a15 15 0 0 0 6.6 6.6l2.2-2.2a1 1 0 0 1 1-.25 11 11 0 0 0 3.6.6 1 1 0 0 1 1 1V20a1 1 0 0 1-1 1A17 17 0 0 1 3 4a1 1 0 0 1 1-1h3.5a1 1 0 0 1 1 1 11 11 0 0 0 .6 3.6 1 1 0 0 1-.25 1z"/></svg></span>+1 (555) 014-2290</li>
        <li><span class="ic"><svg width="11" height="9" viewBox="0 0 24 18"><rect width="24" height="18" rx="2" fill="#3f5bf0"/><path d="M1 2l11 8 11-8" fill="none" stroke="#fff" stroke-width="2"/></svg></span>hello@brightmoorlabs.com</li>
        <li><span class="ic"><svg width="9" height="12" viewBox="0 0 18 24"><path fill="#3f5bf0" d="M9 0a9 9 0 0 0-9 9c0 7 9 15 9 15s9-8 9-15a9 9 0 0 0-9-9zm0 12a3 3 0 1 1 0-6 3 3 0 0 1 0 6z"/></svg></span>4820 Harlow Ave Suite 210<br>Riverton, AZ 85099</li>
      </ul>
    </div>
    <div class="col subscribe" style="left:836px">
      <h4>Subscribe</h4>
      <div class="field">
        <span><svg width="10" height="8" viewBox="0 0 24 18"><rect x="1" y="1" width="22" height="16" rx="2" fill="none" stroke="#333" stroke-width="2"/><path d="M1 2l11 8 11-8" fill="none" stroke="#333" stroke-width="2"/></svg>Email Address</span>
        <b><svg width="16" height="14" viewBox="0 0 24 22"><path fill="#fff" d="M0 10L24 0l-4 22-7-6-3 5v-7l10-10-12 8z"/></svg></b>
      </div>
    </div>
    <span class="line"></span>
    <p class="copy">© 2025 &nbsp;/&nbsp; All Rights Reserved</p>
    <div class="social" style="left:996px;top:285px;gap:24px"><span aria-label="Professional network" style="width:18px;height:18px"></span><span aria-label="Social feed" style="width:18px;height:18px"></span></div>
  </footer>

</div>
</body>
</html>
```